We are an online mail order nursery selling live plants who needs a 1 page landing page for an upcom

We are opening a new sister site to our main site. The new site is membership based. We need a landing page for an email campaign that is both attention grabbing and simply luring the customer to click on the learn more about Membership Page : http://www.fernlanecircle.com/pages/membership-info
The landing page will need to have space reserved for a white board presentation. I have attached the video below. The vid will be hosted on Reel barn so we should be able to use the iframe / embed technique. Again our goal is to funnel the customer to http://www.fernlanecircle.com/pages/membership-info where they can get more details.

Target Market(s)

Home owners between the age of 35 and 65 - gardening enthusiast

Industry/Entity Type

Campaign

Number of Pages Required

1 page

Font styles to use
Sans Serif

Requirements
Must have
• space to embed white board video

```html
<!DOCTYPE html>
<html lang="en">
<head>
<meta charset="utf-8">
<title>Fernlane Circle – Gold Membership</title>
<link href="https://fonts.googleapis.com/css2?family=Arimo:ital,wght@0,400;0,700;1,400&display=swap" rel="stylesheet">
<style>
:root{
  --green:#8cc63f;
  --green-dark:#1f5a2e;
  --purple:#6b1a7e;
  --grey-text:#555555;
  --grey-light:#9a9a9a;
  --grey-box:#a9a9a9;
  --rule:#dddddd;
  --white:#ffffff;
}
*{margin:0;padding:0;box-sizing:border-box}
html,body{width:1200px;height:2164px;overflow:hidden;background:var(--white)}
body{font-family:"Arimo",Arial,sans-serif;color:var(--grey-text);position:relative}
.abs{position:absolute}
.brand{left:34px;top:48px;display:flex;align-items:center;gap:22px}
.brand-mark{width:84px;height:84px;background:var(--green-dark)}
.brand-name{font-size:46px;font-weight:400;color:var(--green-dark);letter-spacing:1px;line-height:1}
.phone{right:34px;top:92px;display:flex;align-items:center;gap:14px;font-size:40px;font-weight:700;color:#666}
.rule{left:34px;width:1132px;height:2px;background:var(--rule)}
.video{left:34px;top:242px;width:756px;height:458px;background:#ececec;border:2px solid #d6d6d6}
.video-art{position:absolute;left:0;top:0;width:100%;height:440px;background:radial-gradient(ellipse at center,#f6f6f6 0%,#e6e6e6 70%)}
.video-bar{position:absolute;left:0;bottom:0;width:100%;height:16px;background:#6d6d6d}
.video-progress{position:absolute;left:8px;bottom:5px;width:700px;height:5px;background:#9c9c9c}
.video-knob{position:absolute;left:100px;bottom:3px;width:14px;height:9px;background:#ddd;border-radius:2px}
.promo{left:834px;top:240px;width:332px;height:152px;background:var(--green);color:var(--white)}
.promo-get{position:absolute;left:8px;top:4px;font-size:22px}
.promo-pct{position:absolute;right:8px;top:-4px;font-size:124px;font-weight:700;letter-spacing:-4px;line-height:1}
.promo-sub{position:absolute;left:0;right:0;bottom:6px;text-align:center;font-size:17px}
.hurry{left:936px;top:394px;width:230px;height:74px;background:var(--grey-box);color:var(--white);text-align:right;padding-right:8px}
.hurry b{display:block;font-size:48px;line-height:48px}
.hurry span{font-size:14px}
.promo-copy{left:850px;top:482px;width:316px;text-align:right;font-size:17px;line-height:21px;color:#444}
.btn{display:flex;align-items:center;justify-content:center;color:var(--white);font-size:28px}
.btn-learn{left:860px;top:644px;width:306px;height:56px;background:var(--purple);border-radius:4px}
.band{background:var(--purple);color:var(--white);font-size:38px;font-weight:700;padding-left:18px;display:flex;align-items:center;height:60px}
.about-band{left:34px;top:760px;width:656px}
.about-photo{left:714px;top:760px;width:452px;height:424px;background:radial-gradient(ellipse at 60% 40%,#f0b98a 0%,#d9895a 60%,#b9683f 100%)}
.about-head{left:34px;top:846px;font-size:54px;font-weight:700;color:var(--green)}
.about-sub{left:34px;top:914px;font-size:34px;font-style:italic;color:#a0a0a0}
.about-rule{left:34px;top:966px;width:620px;height:2px;background:var(--rule)}
.about-copy{left:34px;top:984px;width:620px;font-size:22px;line-height:28px;color:#444}
.blog-band{left:34px;top:1244px;width:1132px}
.post-thumb{left:34px;width:146px;height:144px}
.post-title{left:200px;font-size:31px;color:var(--green)}
.post-copy{left:202px;width:966px;font-size:22px;line-height:28px;color:#444}
.read-more{left:200px;font-size:17px;font-weight:700;color:var(--purple)}
.banner{left:34px;top:1762px;width:1132px;height:230px;background:linear-gradient(90deg,#ffffff 0%,#f5f8e6 45%,#e3efb0 70%,#c9e07a 100%)}
.banner-head{left:34px;top:1792px;font-size:42px;font-weight:700;color:var(--purple);letter-spacing:2px}
.banner-sub{left:34px;top:1846px;font-size:33px;color:#555}
.btn-find{left:34px;top:1902px;width:248px;height:56px;background:var(--green);border-radius:3px}
.foot-nav{left:36px;top:2036px;font-size:22px;color:#8a8a8a}
.foot-nav span{margin:0 10px;color:#bbb}
.social{right:34px;top:2040px;display:flex;gap:20px}
.social i{display:block;width:30px;height:30px;background:var(--green);border-radius:5px}
.unsub{left:0;width:1200px;top:2112px;text-align:center;font-size:17px;color:#333}
.unsub a{color:var(--green);text-decoration:none}
</style>
</head>
<body>
<header>
  <div class="abs brand"><div class="brand-mark"></div><div class="brand-name">FERNLANE CIRCLE</div></div>
  <div class="abs phone">
    <svg width="36" height="36" viewBox="0 0 36 36"><rect width="36" height="36" rx="6" fill="#8cc63f"/><path d="M12 8c1 0 2 3 2.6 5 .3 1-1.5 2-1.3 2.8.8 2.5 3 4.9 5.6 5.9.8.3 1.8-1.6 2.8-1.3 2 .6 5 1.6 5 2.6 0 2-2 4-4 4C15 27 9 21 9 12c0-2 1.5-4 3-4z" fill="#fff"/></svg>
    888-555-0142
  </div>
</header>
<div class="abs rule" style="top:182px"></div>

<section>
  <div class="abs video">
    <div class="video-art" role="img" aria-label="Video poster: laptop showing the whiteboard presentation with a play button"></div>
    <div class="video-bar"><div class="video-progress"></div><div class="video-knob"></div></div>
  </div>
  <div class="abs promo"><span class="promo-get">GET</span><span class="promo-pct">30%</span><span class="promo-sub">DISCOUNT WITH EVERY PURCHASE</span></div>
  <div class="abs hurry"><b>HURRY!</b><span>START YOUR DREAM GARDEN</span></div>
  <p class="abs promo-copy">With our $30 per year Gold Membership you are entitled to a 30% discount on top of a 50% discount on all items in the catalog with every purchase.. no more waiting for coupon offers.</p>
  <a class="abs btn btn-learn">LEARN MORE!</a>
</section>

<section>
  <h2 class="abs band about-band">ABOUT US</h2>
  <h3 class="abs about-head">WE GROW PLANTS!</h3>
  <p class="abs about-sub">Beautiful, Healthy, Affordable Plants.</p>
  <div class="abs about-rule"></div>
  <p class="abs about-copy">We have been in the nursery business for 30 years. We got into the mail order business in 2001. We operate one retail garden center and are in process of constructing a second retail location. There is nothing to see at Birchwood Road location (shipping) but if you are in Millbrook. VA stop by and see us. <b>(276-555-0118)</b></p>
  <div class="abs about-photo" role="img" aria-label="Photo of small succulents in terracotta pots with spilled soil"></div>
</section>

<section>
  <h2 class="abs band blog-band">FROM THE BLOG</h2>
  <div class="abs post-thumb" style="top:1334px;background:linear-gradient(135deg,#d6d86a,#5f8f35 60%,#2f5a22)" role="img" aria-label="Photo of variegated hosta leaves"></div>
  <h3 class="abs post-title" style="top:1330px">Holes in Hosta Leaves</h3>
  <p class="abs post-copy" style="top:1370px">Hostas are one of the most reliable, popular, and simple-to-care-for perennials for home gardeners according to US department of agriculture. But experienced gardeners know these plants are not immune some common problems just as faced while growing other plants.</p>
  <a class="abs read-more" style="top:1472px">Read More!</a>
  <div class="abs rule" style="top:1512px"></div>

  <div class="abs post-thumb" style="top:1546px;background:linear-gradient(180deg,#7a5aa8,#6a8a3a 55%,#d8c83a)" role="img" aria-label="Photo of purple and yellow perennial flowers"></div>
  <h3 class="abs post-title" style="top:1542px;left:204px">What is a Perennial?</h3>
  <p class="abs post-copy" style="top:1582px">What Is PerennialHave you come across those beautiful Perennial Flowers and wondered what kind of plant they are? We are going to dicuss them in this context. What are Perennial Plants.Perennials are long lived non-woody plants, herbs and flowers.</p>
  <a class="abs read-more" style="top:1684px">Read More!</a>
  <div class="abs rule" style="top:1734px"></div>
</section>

<section>
  <div class="abs banner" role="img" aria-label="Soft-focus photo of yellow daffodils and green stems"></div>
  <h2 class="abs banner-head">GET A FREE GOLD MEMBERSHIP</h2>
  <p class="abs banner-sub">Saving Money is Equal to Earning Money</p>
  <a class="abs btn btn-find">Find Out How!</a>
</section>

<footer>
  <nav class="abs foot-nav">Home<span>|</span>About Us<span>|</span>Membership<span>|</span>Contact</nav>
  <div class="abs social"><i></i><i></i><i></i><i></i></div>
  <div class="abs rule" style="top:2082px"></div>
  <p class="abs unsub">Don't want to receive email updates? <a>Unsubscribe here</a></p>
</footer>
</body>
</html>
```